Raised Fingerprint Business Card Design

I need a business card design and I would like the image for the business cards to carry on to my stationary and website. My business is Forensic Consulting. I will be providing services to prosecuting and defense attorneys as well as law enforcement agencies in the areas of latent print comparison, crime scene investigations, and forensic training. I am looking for a color scheme of red, black, and silver. I would like a fingerprint that is raised and the text to be raised to some degree depending on your recommendations. with a fingerprint glass. I would like the card to include the business name, my name the deignation CLPE after it, phone number, web address, and physical address. I would like the phrase "veritas aequitas " placed discretely at the bottome of the card-subtle/not too bold.

Target Market(s)

Attorneys and law enforcement agencies

Industry/Entity Type

Business

Contact Information for Business Card

Delia Forsythe, CLPE
Brightwell Evidence Group, LLC
P.O. Box 583172 Sacramento, CA 95817
916.428.3071
www.brightwellevidencegroup.example
brightwellevidence@mailbox.example

Colors
ec1f27

Requirements
Must have
• Fingerprint and old fashioned handheld magnifying glass (Sherlock Holmes style.
• The Latin phrase listed above placed at the bottom of the front of the card discreetly.
Nice to have
• The fingerprint ridges (black lines) raised so the customer can feel it the texture.
• Raised lettering for either my name or the company name.
Should not have
• None that I can think of now.

```html
<!DOCTYPE html>
<html lang="en">
<head>
<meta charset="utf-8">
<title>Brightwell Evidence Group — Business Card</title>
<link rel="stylesheet" href="https://fonts.googleapis.com/css2?family=Arimo:wght@400;700&family=Raleway:wght@300;500&display=swap">
<style>
  :root {
    --backdrop: #3a3838;
    --card: #161616;
    --card-deep: #0b0b0b;
    --accent-red: #ec1f27;
    --white: #f2f2f2;
    --silver: #c9c9c9;
    --muted: #8a8a8a;
    --contact-blue: #2a92e4;
  }
  * { margin: 0; padding: 0; box-sizing: border-box; }
  html, body { width: 1200px; height: 1000px; overflow: hidden; }
  body {
    background: var(--backdrop);
    font-family: "Arimo", Arial, sans-serif;
    position: relative;
  }
  .card {
    position: absolute;
    width: 560px;
    height: 320px;
    background: radial-gradient(ellipse at 50% 40%, #222 0%, var(--card) 55%, var(--card-deep) 100%);
    box-shadow: 0 18px 40px rgba(0,0,0,0.55);
    overflow: hidden;
  }
  .card::after {
    content: "";
    position: absolute;
    left: 0; right: 0; bottom: 0;
    height: 9px;
    background: linear-gradient(180deg, #ff3a40, var(--accent-red) 50%, #a8141a);
  }
  .card--front { left: 60px; top: 150px; }
  .card--back { left: 580px; top: 500px; }

  .fingerprint-area {
    position: absolute;
    left: 190px; top: 50px;
    width: 180px; height: 180px;
    border-radius: 50%;
    background: radial-gradient(circle, #2c2c2c 0%, #1f1f1f 55%, rgba(22,22,22,0) 72%);
  }
  .company-line {
    position: absolute;
    left: 0; right: 0; top: 148px;
    text-align: center;
    color: var(--white);
    font-weight: 700;
    font-size: 17px;
    letter-spacing: 0.5px;
    white-space: nowrap;
  }
  .company-line .designation { margin-right: 8px; }
  .motto {
    position: absolute;
    left: 0; right: 0; top: 180px;
    text-align: center;
    color: var(--muted);
    font-size: 12px;
    letter-spacing: 6px;
  }

  .card--back .company-line {
    left: 28px; right: auto; top: 30px;
    text-align: left;
    font-size: 14px;
  }
  .divider { position: absolute; left: 0; top: 0; }
  .holder-name {
    position: absolute;
    right: 78px; top: 78px;
    font-family: "Raleway", Arial, sans-serif;
    font-size: 28px;
    color: var(--silver);
  }
  .holder-name .given { font-weight: 500; color: var(--white); }
  .holder-name .family { font-weight: 300; }
  .contact-list {
    position: absolute;
    right: 78px; top: 128px;
    list-style: none;
    text-align: right;
    color: var(--contact-blue);
    font-weight: 700;
  }
  .contact-list .phone { font-size: 22px; }
  .contact-list .email { font-size: 14px; margin-top: 4px; }
  .contact-list .web { font-size: 13px; margin-top: 4px; }
  .contact-list .address { font-size: 11px; font-weight: 400; margin-top: 6px; }
  .icon-column {
    position: absolute;
    right: 28px; top: 70px;
    display: flex; flex-direction: column; gap: 6px;
  }
  .icon-column svg { display: block; }
</style>
</head>
<body>

<section class="card card--front">
  <div class="fingerprint-area" role="img" aria-label="Raised fingerprint with a handheld magnifying glass"></div>
  <p class="company-line"><span class="designation">CLPE</span>BRIGHTWELL EVIDENCE GROUP, LLC</p>
  <p class="motto">veritas aequitas</p>
</section>

<section class="card card--back">
  <p class="company-line"><span class="designation">CLPE</span>BRIGHTWELL EVIDENCE GROUP, LLC</p>
  <svg class="divider" width="560" height="320" aria-hidden="true">
    <line x1="40" y1="58" x2="480" y2="58" stroke="#555" stroke-width="1"/>
    <line x1="220" y1="118" x2="480" y2="118" stroke="#777" stroke-width="1"/>
    <line x1="300" y1="118" x2="110" y2="290" stroke="#666" stroke-width="1"/>
  </svg>
  <p class="holder-name"><span class="given">Delia</span><span class="family">Forsythe</span></p>
  <ul class="contact-list">
    <li class="phone">916.428.3071</li>
    <li class="email">brightwellevidence@mailbox.example</li>
    <li class="web">www.brightwellevidencegroup.example</li>
    <li class="address">P.O. Box 583172 Sacramento, CA 95817</li>
  </ul>
  <div class="icon-column" aria-hidden="true">
    <svg width="22" height="22" viewBox="0 0 22 22"><circle cx="11" cy="11" r="10" fill="#f2f2f2"/><path d="M7 6 l3 0 l1 3 l-1.5 1 a7 7 0 0 0 3 3 l1-1.5 l3 1 l0 3 a9 9 0 0 1 -9.5-9.5z" fill="#161616"/></svg>
    <svg width="22" height="22" viewBox="0 0 22 22"><circle cx="11" cy="11" r="10" fill="#f2f2f2"/><rect x="5.5" y="7" width="11" height="8" fill="none" stroke="#161616" stroke-width="1.4"/><path d="M5.5 7 L11 11.5 L16.5 7" fill="none" stroke="#161616" stroke-width="1.4"/></svg>
    <svg width="22" height="22" viewBox="0 0 22 22"><circle cx="11" cy="11" r="10" fill="#f2f2f2"/><circle cx="11" cy="11" r="6" fill="none" stroke="#161616" stroke-width="1.3"/><ellipse cx="11" cy="11" rx="2.6" ry="6" fill="none" stroke="#161616" stroke-width="1.1"/><line x1="5" y1="11" x2="17" y2="11" stroke="#161616" stroke-width="1.1"/></svg>
    <svg width="22" height="22" viewBox="0 0 22 22"><circle cx="11" cy="11" r="10" fill="#f2f2f2"/><path d="M5 11 L11 5.5 L17 11 M7 10 V16 H15 V10" fill="none" stroke="#161616" stroke-width="1.4"/></svg>
  </div>
</section>

</body>
</html>
```